Informational Trifold Flyer to Highlight Our After-School Program Curriculum

We need a trifold to hand out to families at our open house events that highlights our programs and curriculum. We provide quality, nationally recognized, award winning child development programs and after school care affordable to every family at any income level. Our programs include curriculum in Education & Career Development, STEM, the Arts, Academic Support, Character & Leadership, Health & Life Skills, Sports & Recreation.

Our curriculum is designed to be fun AND purposeful.

Our target market is parents of children ages 4-13 years old of every socioeconomic background. The brochure needs to be inclusive, eye-catching, family friendly, professional and informative.

I'm uploading our current curriculum guide for a sense of the flyer's CONTENT ONLY. Please DO NOT copy the design in the Curriculum Guide upload - we plan to redesign it soon. Please DO USE the Success Statistics in the Curriculum Guide.

I'm also uploading some of our recent flyer designs for a sense of the look and feel that we like. Also uploading our logo, some other branded assets, and a branding guideline that can be referred to for colors, fonts and logo spacing. The logo is the only required asset. The colors listed in the guideline are not required. The brand fonts are not required either but using them is a good idea, unless they just don't work with your creative vision.

I can provide logo files and other assets as psd files for final flyer.

We have around 10 flyers we need designed each year so this project can lead to regular, ongoing work.

Target Market(s)

Parents of children ages 4-13

Industry/Entity Type

Non-profit child care and child development

Font styles to use
Serif
Sans Serif
Other font styles liked:
• Franklin Gothic Book URW - Book, Franklin Gothic URW - Demi, Museo Slab - 1000, Helvetica - Regular, Arial Regular

Requirements
Must have
• Logo. Inclusive, family friendly. Ability to edit brochure based on location. Success Statistics Highlighted (see curriculum guide for content). Room for list of core programs. Quotes from parents. Register online: URL (will vary by location).
Nice to have
• It would be nice to be able to feature a few different aspects of program in detail, or show a curriculum project. Can provide content for such.
Should not have
• Anything that is not inclusive or family friendly.

```html
<!DOCTYPE html>
<html lang="en">
<head>
<meta charset="utf-8">
<title>Rise Up Academy Trifold</title>
<link rel="stylesheet" href="https://fonts.googleapis.com/css2?family=Montserrat:wght@400;700;800&family=Open+Sans:wght@400;600;700&display=swap">
<style>
:root{
  --bg:#4a4a4c;
  --purple:#5a2b99;
  --purple-deep:#45238a;
  --blue:#1d63c9;
  --blue-bright:#0a8ad6;
  --green:#3fb04b;
  --white:#ffffff;
  --paper:#f1f1f4;
  --photo-a:#c98f6a;
  --photo-b:#5c7fa8;
}
*{box-sizing:border-box;margin:0;padding:0}
html,body{width:1200px;height:675px;overflow:hidden;background:var(--bg)}
body{font-family:"Open Sans",Arial,sans-serif;color:var(--white);position:relative}
.sheet{position:absolute;top:117px;width:570px;height:440px;overflow:hidden;box-shadow:0 10px 30px rgba(0,0,0,.45)}
.sheet--inside{left:20px}
.sheet--outside{left:610px}
.panel{position:absolute;top:0;width:190px;height:440px;overflow:hidden}
.panel--1{left:0}.panel--2{left:190px}.panel--3{left:380px}
.bg-shapes{position:absolute;inset:0}
.h-title{font-family:"Montserrat",Arial,sans-serif;font-weight:400;font-size:17px;letter-spacing:.5px;white-space:nowrap}
.h-title b{font-weight:800}
.body-text{font-size:7.2px;line-height:1.4}
.photo{position:absolute;border-radius:50%;background:radial-gradient(circle at 40% 35%,var(--photo-a),var(--photo-b) 75%)}
.mission{position:absolute;left:16px;top:48px;width:108px}
.mission .body-text{margin-top:6px;font-size:7.4px}
.stat{position:absolute;left:26px;top:376px;color:var(--purple);display:flex;align-items:flex-start;gap:5px}
.stat-number{font-family:"Montserrat",Arial,sans-serif;font-weight:800;font-size:32px;line-height:1}
.stat-number sup{font-size:14px;font-weight:400}
.stat-label{font-size:7.4px;line-height:1.3;margin-top:3px;white-space:nowrap}
.slogan{position:absolute;left:190px;top:38px;color:var(--purple);font-family:"Montserrat",Arial,sans-serif;text-align:right;width:160px}
.slogan-small{font-size:9px;font-weight:400;letter-spacing:.5px}
.slogan-big{font-size:20px;font-weight:800;color:var(--blue-bright);line-height:1}
.mission-photo{left:105px;top:118px;width:220px;height:220px}
.name-disc{position:absolute;left:175px;top:188px;width:80px;height:80px;border-radius:50%;background:var(--white);display:flex;align-items:center;justify-content:center;text-align:center;color:var(--blue);font-family:"Montserrat",Arial,sans-serif;font-weight:800;font-size:10px;line-height:1.1}
.belief{position:absolute;left:225px;top:346px;width:150px;text-align:right;font-family:"Montserrat",Arial,sans-serif;font-weight:700;font-size:8.6px;line-height:1.3}
.programs{position:absolute;left:12px;top:22px;width:168px}
.programs .body-text{margin-top:5px;font-size:6.4px}
.programs .lead{font-weight:700;margin-top:4px}
.rule{height:1px;background:rgba(255,255,255,.5);margin:10px 0 8px 60px}
.focus{display:flex;gap:8px}
.focus-badge{flex:none;width:40px;height:40px;border-radius:50%;border:1.5px solid var(--white);display:flex;align-items:center;justify-content:center;text-align:center;font-size:6.5px;font-weight:700;line-height:1.1;outline:1px dashed rgba(255,255,255,.6);outline-offset:3px}
.focus-list{list-style:none;margin-top:26px;font-size:6.2px;line-height:1.35}
.focus-list li{display:flex;gap:6px;margin-bottom:7px}
.focus-list b{font-weight:700}
.say-photo{left:30px;top:-40px;width:140px;height:140px}
.quote-mark{position:absolute;left:18px;top:100px;font-family:"Montserrat",Arial,sans-serif;font-weight:800;font-size:56px;line-height:1;color:var(--white)}
.say{position:absolute;left:18px;top:148px;width:160px}
.quote{font-size:6.8px;line-height:1.4;margin-top:8px}
.quote cite{display:block;font-style:normal;font-weight:700;margin-top:2px}
.back-name{position:absolute;left:22px;top:48px;font-family:"Montserrat",Arial,sans-serif;font-weight:800;font-size:15px;display:flex;align-items:center;gap:6px;white-space:nowrap}
.back-name i{width:10px;height:10px;border-radius:50%;background:var(--white);display:block}
.contact{position:absolute;left:22px;top:90px;list-style:none;font-size:6.8px;line-height:1}
.contact li{display:flex;align-items:center;gap:6px;margin-bottom:7px}
.cover-name{position:absolute;left:0;width:190px;top:64px;font-family:"Montserrat",Arial,sans-serif;font-weight:800;font-size:16px;display:flex;align-items:center;justify-content:center;gap:6px;white-space:nowrap}
.cover-name i{width:11px;height:11px;border-radius:50%;background:var(--white);display:block}
.cover-tags{position:absolute;left:0;width:190px;top:96px;text-align:center;font-family:"Montserrat",Arial,sans-serif;font-weight:700;font-size:8.4px;line-height:1.5}
.cover-photo{left:-30px;top:190px;width:260px;height:260px;border:4px solid var(--white)}
.cover-inset{left:95px;top:330px;width:110px;height:110px;border:4px solid var(--white);background:radial-gradient(circle at 50% 40%,#d9b08f,#3c5f8a 75%)}
</style>
</head>
<body>

<section class="sheet sheet--inside" aria-label="Inside spread">
  <svg class="bg-shapes" width="570" height="440" viewBox="0 0 570 440" aria-hidden="true">
    <defs>
      <linearGradient id="progGrad" x1="0" y1="1" x2="1" y2="0">
        <stop offset="0" stop-color="#3e37a8"/>
        <stop offset="1" stop-color="#0a8ad6"/>
      </linearGradient>
      <linearGradient id="midGrad" x1="0" y1="0" x2="1" y2="0">
        <stop offset="0" stop-color="#5a2b99"/>
        <stop offset="1" stop-color="#4a35a6"/>
      </linearGradient>
    </defs>
    <rect width="570" height="440" fill="url(#progGrad)"/>
    <rect width="380" height="440" fill="url(#midGrad)"/>
    <polygon points="200,0 380,0 380,30 140,440 20,440 0,420 0,0" fill="#5a2b99" opacity="0"/>
    <polygon points="200,0 380,0 380,30 140,440 20,440 0,420" fill="#f1f1f4"/>
    <rect x="30" y="250" width="64" height="13" rx="6.5" transform="rotate(-40 62 256)" fill="#7a52b8" opacity=".7"/>
    <circle cx="290" cy="270" r="12" fill="#2f7fd8" opacity=".7"/>
  </svg>

  <div class="mission">
    <h2 class="h-title">OUR <b>MISSION</b></h2>
    <p class="body-text">To inspire and enable all young people, especially those who need us most, to realize their full potential as productive, caring, responsible citizens.</p>
  </div>

  <div class="slogan">
    <p class="slogan-small">WHEN SCHOOL'S OUT</p>
    <p class="slogan-big">WE'RE IN</p>
  </div>

  <div class="photo mission-photo" role="img" aria-label="Photo collage of children and a mentor working together on laptops"></div>
  <div class="name-disc">Rise Up<br>Academy</div>

  <p class="belief">We believe that every child has greatness inside of him/her and our job is to help that greatness shine in a fun and purposeful way</p>

  <div class="stat">
    <span class="stat-number">98<sup>%</sup></span>
    <span class="stat-label">of our participants<br>plan to go beyond<br>high school</span>
  </div>

  <div class="panel panel--3">
    <div class="programs">
      <h2 class="h-title">OUR <b>PROGRAMS</b></h2>
      <p class="body-text">Rise Up Academy is the after school program of the Youth Clubs of the Heartland. We have a lineup of tested and nationally proven programs that address today's most pressing youth issues, teaching young people the skills they need to succeed in life.</p>
      <p class="body-text lead">We offer programs with a purpose in an affordable, safe, fun environment.</p>
      <div class="rule"></div>
      <div class="focus">
        <div class="focus-badge">Core<br>Focus<br>Areas</div>
        <ul class="focus-list">
          <li><span><b>Character &amp; Leadership:</b> Developed to help youth become responsible, caring citizens and acquire skills for participating in the democratic process</span></li>
          <li><span><b>Education &amp; Career Development:</b> designed to ensure that all Club members graduate from high school on time, ready for a post-secondary education and a 21st-century career</span></li>
          <li><span><b>Sports, Fitness, &amp; Recreation:</b> strives to improve the overall health of Club members by increasing their daily physical activity</span></li>
          <li><span><b>Health &amp; Life Skills:</b> To develop young people's capacity to engage in positive behaviors that nurture their own well being, set personal goals and live successfully as self sufficient adults</span></li>
          <li><span><b>The Arts:</b> designed to foster creativity in young people, and give them outlets for self-expression</span></li>
        </ul>
      </div>
    </div>
  </div>
</section>

<section class="sheet sheet--outside" aria-label="Outside spread">
  <svg class="bg-shapes" width="570" height="440" viewBox="0 0 570 440" aria-hidden="true">
    <defs>
      <linearGradient id="backGrad" x1="0" y1="1" x2="1" y2="0">
        <stop offset="0" stop-color="#5a2b99"/>
        <stop offset=".45" stop-color="#3fb04b"/>
        <stop offset="1" stop-color="#1d63c9"/>
      </linearGradient>
      <linearGradient id="coverGrad" x1="0" y1="0" x2="0" y2="1">
        <stop offset="0" stop-color="#0a8ad6"/>
        <stop offset="1" stop-color="#1d4fbf"/>
      </linearGradient>
    </defs>
    <rect width="190" height="440" fill="#5a2b99"/>
    <rect x="190" width="190" height="440" fill="url(#backGrad)"/>
    <polygon points="150,0 190,0 190,440 130,440" fill="#4a2d9e" opacity=".6"/>
    <rect x="380" width="190" height="440" fill="url(#coverGrad)"/>
    <rect x="150" y="120" width="110" height="14" rx="7" transform="rotate(-40 205 127)" fill="#2fb3a3"/>
    <circle cx="120" cy="385" r="13" fill="#7a52b8" opacity=".7"/>
    <circle cx="95" cy="390" r="5" fill="#7a52b8" opacity=".7"/>
    <circle cx="405" cy="28" r="9" fill="#6ac04c"/>
    <circle cx="425" cy="22" r="3" fill="#f2b233"/>
    <circle cx="420" cy="38" r="3" fill="#9a6cd8"/>
    <circle cx="440" cy="28" r="5" fill="#5aa9ec"/>
  </svg>

  <div class="photo say-photo" role="img" aria-label="Photo of two girls painting at an easel"></div>
  <div class="quote-mark">&ldquo;</div>
  <div class="say">
    <h2 class="h-title">THEIR <b>SAY</b></h2>
    <p class="quote">My son loves the after care providers and I feel this is what makes the program a success. They genuinely care for the members. I don't have to worry when my child is there - he has assistance with homework and activities that help him grow.<cite>Club Parent</cite></p>
    <p class="quote">I like that my daughter loves the program so much that she doesn't want to leave when I go to pick her up.<cite>Club Parent</cite></p>
    <p class="quote">I like the friendly and understanding staff members. I love that my child enjoys the after school program and that they set aside time for homework.<cite>Club Parent</cite></p>
  </div>

  <div class="panel panel--2">
    <p class="back-name"><i></i>Rise Up Academy</p>
    <ul class="contact">
      <li><svg width="8" height="8" viewBox="0 0 10 10"><path d="M2 1l2 2-1 1.5a5 5 0 0 0 2.5 2.5L7 6l2 2-1.5 1.5C4 9 1 6 .5 2.5z" fill="#fff"/></svg>555.014.2200</li>
      <li><svg width="8" height="8" viewBox="0 0 10 10"><rect x=".5" y="2" width="9" height="6" fill="none" stroke="#fff"/><path d="M.5 2l4.5 3.5L9.5 2" fill="none" stroke="#fff"/></svg>hello@riseupacademy.org</li>
      <li><svg width="8" height="8" viewBox="0 0 10 10"><circle cx="5" cy="5" r="4.3" fill="none" stroke="#fff"/><path d="M.7 5h8.6M5 .7c2 2.5 2 6 0 8.6M5 .7c-2 2.5-2 6 0 8.6" fill="none" stroke="#fff" stroke-width=".7"/></svg>www.riseupacademy.org</li>
    </ul>
  </div>

  <div class="panel panel--3">
    <p class="cover-name"><i></i>Rise Up Academy</p>
    <p class="cover-tags">Academic Success<br>Good Character &amp; Citizenship<br>Healthy Lifestyles</p>
    <div class="photo cover-photo" role="img" aria-label="Photo of smiling children playing and drawing together"></div>
    <div class="photo cover-inset" role="img" aria-label="Photo of a child concentrating on schoolwork"></div>
  </div>
</section>

</body>
</html>
```